Stylish business cards for KX7

To create an appealing and professional business card design for a WOMEN Owned Construction Supply Company.
2 sided card. Incorporate brand elements, curvy, colorful, sleek and bright. No solid white background. attached samples of styles added shapes/ribbons. Want something with that WOW that looks awesome, factor. It is a new logo, so feel free to mess with logo colors in the blue and teal factors that can look good with both dark and light background. If you want to try a watermark with just the KX7, without the "Supply" that might look cool to.

Industry/Entity Type

Women owned construction supply company

Contact Information for Business Card

Name, Title, and phone number and email, web page. maybe spot for qr code.

Font styles to use
Sans Serif

Requirements
Nice to have
• would love to see colors, maybe stylish ribbon dividers or some sort of 2 or 3 tone color card that compliments logo.
Should not have
• Please do not have all white background. Do not include Home/reale state/ or building images.

```html
<!DOCTYPE html>
<html lang="en">
<head>
<meta charset="utf-8">
<title>KX7 Supply – Business Cards</title>
<link href="https://fonts.googleapis.com/css2?family=Roboto:wght@400;500&display=swap" rel="stylesheet">
<style>
  :root {
    --stage: #7b7b7b;
    --navy: #1a3a5c;
    --teal: #1e93b9;
    --white: #ffffff;
    --shadow: rgba(0, 0, 0, 0.35);
  }
  html, body {
    margin: 0;
    padding: 0;
    width: 1199px;
    height: 1200px;
    overflow: hidden;
    background: var(--stage);
    font-family: "Roboto", Arial, sans-serif;
  }
  .card {
    position: absolute;
    left: 172px;
    width: 855px;
    height: 500px;
    overflow: hidden;
    box-shadow: 6px 10px 14px var(--shadow);
  }
  .card-front { top: 81px; background: var(--white); }
  .card-back {
    top: 618px;
    background: linear-gradient(90deg, var(--navy) 0%, var(--teal) 100%);
  }
  .front-shapes { position: absolute; inset: 0; width: 855px; height: 500px; }
  .brand-name {
    position: absolute;
    margin: 0;
    font-weight: 500;
    letter-spacing: 1px;
    white-space: nowrap;
    transform: translate(-50%, -50%);
  }
  .card-front .brand-name { left: 640px; top: 180px; font-size: 58px; color: var(--navy); }
  .card-back .brand-name { left: 427px; top: 250px; font-size: 72px; color: var(--white); }
  .holder-name {
    position: absolute;
    left: 62px;
    top: 288px;
    margin: 0;
    font-size: 35px;
    font-weight: 500;
    color: var(--white);
  }
  .contact-list {
    position: absolute;
    margin: 0;
    padding: 0;
    list-style: none;
    color: var(--white);
    font-size: 22px;
    line-height: 34px;
  }
  .contact-list.left { left: 62px; top: 357px; }
  .contact-list.right { left: 512px; top: 357px; }
  .contact-list li { display: flex; align-items: flex-start; gap: 10px; }
  .contact-icon { width: 20px; height: 20px; margin-top: 7px; flex: none; }
  .address-dot {
    width: 20px; height: 20px; border-radius: 50%;
    background: var(--teal); margin-top: 7px; flex: none;
  }
  .address-lines { display: block; }
</style>
</head>
<body>

<section class="card card-front" aria-label="Business card front">
  <svg class="front-shapes" viewBox="0 0 855 500" aria-hidden="true">
    <path fill="var(--teal)" d="M0,0 H310 C290,22 240,28 200,24 C150,20 80,10 0,0 Z"/>
    <path fill="var(--teal)" d="M400,0 C420,22 470,32 520,30 C580,28 620,14 635,0 Z"/>
    <path fill="var(--navy)" d="M0,0 C120,10 230,40 250,120 C262,190 290,225 400,235 C470,242 472,290 540,300 C650,315 820,322 855,392 V500 H0 Z"/>
  </svg>

  <p class="brand-name">KX7 Supply</p>

  <h1 class="holder-name">Dana Reyes</h1>

  <ul class="contact-list left">
    <li>
      <svg class="contact-icon" viewBox="0 0 20 20" aria-hidden="true">
        <circle cx="10" cy="10" r="10" fill="var(--white)"/>
        <path fill="var(--navy)" d="M6.2 4.8l1.8-.4 1.1 2.6-1.2 1c.6 1.3 1.5 2.2 2.8 2.8l1-1.2 2.6 1.1-.4 1.8c-.1.5-.6.8-1.1.8C9 13.2 6.8 11 5.4 5.9c0-.5.3-1 .8-1.1z"/>
      </svg>
      <span>555-0142-0000</span>
    </li>
    <li>
      <svg class="contact-icon" viewBox="0 0 20 20" aria-hidden="true">
        <circle cx="10" cy="10" r="10" fill="var(--white)"/>
        <rect x="5" y="6.5" width="10" height="7" rx="1" fill="var(--teal)"/>
        <path d="M5.5 7.2L10 10.5l4.5-3.3" fill="none" stroke="var(--white)" stroke-width="1"/>
      </svg>
      <span>info@kx7supply.com</span>
    </li>
  </ul>

  <ul class="contact-list right">
    <li>
      <span class="address-dot" aria-hidden="true"></span>
      <span class="address-lines">418/B, Harbor Lane,<br>Pincode-604213</span>
    </li>
  </ul>
</section>

<section class="card card-back" aria-label="Business card back">
  <p class="brand-name">KX7 Supply</p>
</section>

</body>
</html>
```